Harbor Crest Solutions Letterhead Design

The project name sums it up. Just need a professional letterhead design / template we can use in our marketing folders.

Here's the address / contact info for the letterhead: Harbor Crest Solutions 4817 Maple Ridge Dr Suite 150 League City, Texas 77419 346-508-7364 www.harborcrestsolutions.us support@harborcrestsolutions.us

```html
<!DOCTYPE html>
<html lang="en">
<head>
<meta charset="utf-8">
<title>Harbor Crest Solutions Letterhead</title>
<link rel="stylesheet" href="https://fonts.googleapis.com/css2?family=Source+Sans+3:wght@400;600;700&family=Roboto:wght@500;700&family=Open+Sans:wght@700&family=Great+Vibes&display=swap">
<style>
  :root {
    --brand-blue: #0b4ea2;
    --rule-grey: #777777;
    --ink: #231f20;
    --accent-red: #e0202a;
    --footer-grey: #555a60;
    --paper: #ffffff;
  }
  * { margin: 0; padding: 0; box-sizing: border-box; }
  html, body { width: 927px; height: 1200px; overflow: hidden; background: var(--paper); }
  .page {
    position: relative; width: 927px; height: 1200px;
    font-family: "Source Sans 3", "Myriad Pro", sans-serif; color: var(--ink);
  }
  .brand { position: absolute; left: 60px; top: 68px; display: flex; align-items: center; gap: 12px; }
  .brand-mark { width: 34px; height: 34px; background: var(--ink); }
  .brand-name {
    font-family: "Source Sans 3", sans-serif; font-weight: 700; font-size: 30px;
    color: var(--ink); letter-spacing: 0.2px; line-height: 1;
  }
  .rule { position: absolute; height: 5px; display: flex; }
  .rule .blue { background: var(--brand-blue); }
  .rule .grey { background: var(--rule-grey); flex: 1; }
  .rule-head { left: 153px; top: 136px; width: 713px; }
  .rule-head .blue { width: 171px; }
  .rule-foot { left: 58px; top: 1079px; width: 808px; }
  .rule-foot .blue { width: 283px; }

  .sender { position: absolute; left: 98px; top: 204px; }
  .sender-name { color: var(--brand-blue); font-size: 17px; line-height: 1; }
  .sender-role { font-size: 12.5px; margin-top: 13px; line-height: 1; }
  .contact-list { list-style: none; margin-top: 8px; font-size: 15px; }
  .contact-list li { height: 25px; line-height: 25px; white-space: nowrap; }
  .contact-list b { display: inline-block; width: 29px; font-weight: 700; }
  .contact-list .red { color: var(--accent-red); }
  .letter-date { position: absolute; right: 101px; top: 284px; font-size: 15px; }

  .letter-body { position: absolute; left: 99px; top: 358px; font-size: 15.3px; }
  .letter-body p { margin-bottom: 32px; }
  .letter-body span { display: block; height: 32px; line-height: 32px; white-space: nowrap; }

  .signoff { position: absolute; left: 98px; top: 928px; }
  .signature { font-family: "Great Vibes", cursive; font-size: 36px; line-height: 1; color: var(--ink); }
  .signer { font-family: "Open Sans", sans-serif; font-weight: 700; font-size: 15px; margin-top: 2px; line-height: 1.2; }
  .signer-role { font-size: 14px; line-height: 1.2; }

  .footer { position: absolute; left: 88px; top: 1095px; width: 740px; font-family: "Roboto", sans-serif; }
  .footer-row { display: flex; align-items: center; white-space: nowrap; color: var(--footer-grey); font-weight: 500; font-size: 16.5px; }
  .footer-row + .footer-row { margin-top: 12px; }
  .footer-name { color: var(--brand-blue); font-weight: 700; font-size: 20px; margin-right: 20px; }
  .footer-item { display: flex; align-items: center; gap: 8px; margin-right: 18px; }
  .footer-item svg { width: 20px; height: 20px; stroke: var(--brand-blue); fill: none; stroke-width: 1.6; }
</style>
</head>
<body>
<div class="page">
  <header class="brand">
    <div class="brand-mark"></div>
    <div class="brand-name">Harbor Crest Solutions</div>
  </header>
  <div class="rule rule-head"><div class="blue"></div><div class="grey"></div></div>

  <section class="sender">
    <div class="sender-name">Daniel Whitford</div>
    <div class="sender-role">Chief Director</div>
    <ul class="contact-list">
      <li><b class="red">A :</b>27 Cedar Point Road Lakeview - 4120</li>
      <li><b>W :</b>hello@samplemail.com, www.samplesite.com</li>
      <li><b class="red">P :</b>+1 - 55012 - 3478</li>
    </ul>
  </section>
  <div class="letter-date">Date, 10 September, 2020</div>

  <main class="letter-body">
    <p>
      <span>This is a sample letter that has been placed to demonstrate typing remat (Your Company). letterhead</span>
      <span>design. When positioned properly, it will serve to work in harmony with all other elements letterhead.</span>
      <span>This letterhead design is meant to project an image</span>
    </p>
    <p>
      <span>This letterhead design is meant project an image of professionalism reliability. By using simple aligen</span>
      <span>we have created a very spacious feeling. The simplicity suggest&nbsp; rengththe spaciousnes contributes h</span>
      <span>aesthetics the layout. These basic qualities along with the (Your Company)</span>
    </p>
    <p>
      <span>look and helps reinforce the (Your Company) brand. letterhead design is meant to project an image p</span>
      <span>design. When positioned properly, it will serve to work in harmony all the other elements letterhead.</span>
      <span>sionalism and reliability.</span>
    </p>
    <p>
      <span>This letterhead design is based on the (Form of your logo) form (Your Company) logo. Each stationery</span>
      <span>we have created a very spacious feeling. The simplicity suggests strength the spaciousnes contribute</span>
      <span>part of the (Form of your logo).</span>
    </p>
  </main>

  <section class="signoff">
    <div class="signature">Daniel Whitford</div>
    <div class="signer">Daniel Whitford</div>
    <div class="signer-role">Manager</div>
  </section>

  <div class="rule rule-foot"><div class="blue"></div><div class="grey"></div></div>
  <footer class="footer">
    <div class="footer-row">
      <span class="footer-name">Harbor Crest Solutions</span>
      <span class="footer-item">
        <svg viewBox="0 0 20 20" aria-hidden="true"><path d="M10 18.5s-6-6.2-6-10.5a6 6 0 0 1 12 0c0 4.3-6 10.5-6 10.5z"/><circle cx="10" cy="8" r="2.3"/></svg>
        4817 Maple Ridge Dr Suite 150 League City, Texas 77419
      </span>
    </div>
    <div class="footer-row">
      <span class="footer-item">
        <svg viewBox="0 0 20 20" aria-hidden="true"><rect x="5" y="1.5" width="10" height="17" rx="1.8"/><line x1="8.5" y1="15.5" x2="11.5" y2="15.5"/></svg>
        346-508-7364
      </span>
      <span class="footer-item">
        <svg viewBox="0 0 20 20" aria-hidden="true"><circle cx="10" cy="10" r="8"/><ellipse cx="10" cy="10" rx="3.5" ry="8"/><line x1="2" y1="10" x2="18" y2="10"/><path d="M3.5 5.8h13M3.5 14.2h13"/></svg>
        www.harborcrestsolutions.us
      </span>
      <span class="footer-item">
        <svg viewBox="0 0 20 20" aria-hidden="true"><rect x="1.5" y="4" width="17" height="12" rx="1"/><path d="M1.5 4.5 10 11l8.5-6.5M1.5 15.5l6-5M18.5 15.5l-6-5"/></svg>
        support@harborcrestsolutions.us
      </span>
    </div>
  </footer>
</div>
</body>
</html>
```